Marwick Ostrand Law website for a law firm

modern clean website for a small boutique law firm. Based in Sacramento, CA and the Bay Area. Practice areas of Family Law, Civil litigation, and Criminal Defense. We already have a logo design as well as attorney pictures to include on page.
Would like images of California included on site.
Would like site to go with Logo that is already designed...blue/grey/white colors.

Industry/Entity Type

Law Firm

Number of Pages Required

5+ page

Requirements
Must have
• I already have several pages of content drafted. Just need the pages with images to input content. Must be clean and modern feel. Want it to reflect California and small boutique feel that is provided personalized legal attention.
• Must have a page where I can blog or post articles on.

```html
<!DOCTYPE html>
<html lang="en">
<head>
<meta charset="utf-8">
<title>Marwick Ostrand Law</title>
<link href="https://fonts.googleapis.com/css2?family=Open+Sans:wght@400;600;700&family=Lato:wght@400;700&display=swap" rel="stylesheet">
<style>
:root{
  --blue:#4a87c8;
  --blue-dark:#3d77b6;
  --ink:#2b2b2b;
  --text:#444;
  --grey-nav:#8a8a8a;
  --grey-bg:#f1f1f1;
  --rule:#bfbfbf;
  --footer:#232323;
  --footer-field:#161616;
  --footer-line:#3a3a3a;
  --white:#fff;
}
*{margin:0;padding:0;box-sizing:border-box}
html,body{width:1200px;height:2284px;overflow:hidden}
body{position:relative;background:var(--white);font-family:"Lato",sans-serif;color:var(--text)}
.abs{position:absolute}

/* top bar */
.topbar{left:0;top:0;width:1200px;height:34px;background:var(--blue);color:var(--white);font-family:"Open Sans",sans-serif;font-size:13px}
.topbar .contacts{position:absolute;left:88px;top:8px;display:flex;align-items:center;gap:8px}
.topbar .contacts svg{width:12px;height:12px;fill:var(--white)}
.topbar .mail{margin-left:18px;display:flex;align-items:center;gap:8px}
.topbar .social{position:absolute;right:88px;top:11px;display:flex;gap:18px}
.topbar .social span{width:11px;height:11px;border-radius:50%;background:var(--white)}

/* header */
.header{left:0;top:34px;width:1200px;height:100px;background:var(--white)}
.brand{position:absolute;left:86px;top:20px;font-family:"Open Sans",sans-serif;font-weight:400;font-size:58px;letter-spacing:2px;color:var(--blue);line-height:60px}
.nav{position:absolute;top:0;left:0;width:100%;height:100%;font-family:"Open Sans",sans-serif;font-size:15.5px;color:var(--grey-nav)}
.nav a{position:absolute;top:40px;text-decoration:none;color:inherit}
.nav a.active{color:var(--blue);font-weight:600}
.nav a.active::after{content:"";position:absolute;left:-4px;right:-4px;top:57px;height:3px;background:var(--blue)}
.nav .caret{font-size:11px;margin-left:3px}

/* hero */
.hero{left:0;top:134px;width:1200px;height:528px;background:linear-gradient(90deg,#3b4a3c 0%,#6b7a8c 30%,#a7b2c4 50%,#5d6c76 75%,#2f3b33 100%)}
.hero-text{position:absolute;right:90px;top:178px;text-align:right;font-family:"Open Sans",sans-serif;font-weight:600;font-size:31px;line-height:46px;letter-spacing:1.5px;color:var(--white);text-shadow:0 2px 4px rgba(0,0,0,.35)}
.hero-cta{position:absolute;left:911px;top:323px;width:202px;height:38px;border:1.5px solid var(--white);color:var(--white);font-family:"Open Sans",sans-serif;font-weight:600;font-size:15px;letter-spacing:.5px;display:flex;align-items:center;justify-content:center}
.hero-arrow{position:absolute;top:250px;width:20px;height:30px}
.hero-arrow path{fill:none;stroke:var(--white);stroke-width:4}

/* sections */
.section-title{position:absolute;left:0;width:1200px;text-align:center;font-family:"Open Sans",sans-serif;font-weight:600;font-size:30px;color:var(--ink);letter-spacing:.5px}
.section-title em{font-style:normal;color:var(--blue)}
.title-rule{position:absolute;left:485px;width:230px;height:1px;background:var(--rule)}
.lead{position:absolute;text-align:center;font-size:13px;line-height:22px;color:var(--text)}

.services{left:0;top:662px;width:1200px;height:395px;background:var(--grey-bg)}
.service{position:absolute;top:198px;width:330px;text-align:center}
.service svg{width:52px;height:52px;fill:var(--blue)}
.service h3{margin-top:12px;font-family:"Open Sans",sans-serif;font-weight:600;font-size:20px;letter-spacing:.5px;color:var(--ink)}
.service p{margin-top:12px;font-size:13px;line-height:23px;color:var(--text)}

.welcome{left:0;top:1057px;width:1200px;height:317px;background:var(--white)}
.btn-outline{position:absolute;border:2px solid var(--blue);color:var(--ink);font-family:"Open Sans",sans-serif;font-size:15px;display:flex;align-items:center;justify-content:center;letter-spacing:.5px}

.video{left:0;top:1374px;width:1200px;height:527px;background:#f3f3f3}
.video-media{position:absolute;left:244px;top:195px;width:716px;height:332px;background:linear-gradient(180deg,#3a3430 0%,#7a4a36 45%,#c69b7d 100%);border-radius:22px 22px 0 0}
.play{position:absolute;left:584px;top:296px;width:42px;height:42px;border-radius:50%;background:rgba(255,255,255,.9)}
.play svg{position:absolute;left:15px;top:12px;width:14px;height:18px;fill:#333}

/* footer */
.footer{left:0;top:1901px;width:1200px;height:335px;background:var(--footer);color:var(--white)}
.footer h4{position:absolute;top:48px;font-family:"Open Sans",sans-serif;font-weight:600;font-size:21px;letter-spacing:.3px}
.footer .divider{position:absolute;top:50px;width:1px;height:230px;background:var(--footer-line)}
.quick-links{position:absolute;left:88px;top:96px;list-style:none;font-family:"Open Sans",sans-serif;font-size:14px;line-height:26.4px}
.contact-list{position:absolute;left:318px;top:96px;font-family:"Open Sans",sans-serif;font-size:13px;line-height:20px}
.contact-row{position:absolute;left:0;display:flex;gap:13px;white-space:nowrap}
.contact-row svg{width:12px;height:14px;fill:#8a8a8a;flex:none;margin-top:3px}
.field{position:absolute;left:559px;width:259px;background:var(--footer-field);border:1px solid var(--footer-line);font-family:"Open Sans",sans-serif;font-size:13px;color:#ddd;padding:9px 16px}
.submit{position:absolute;left:560px;top:246px;width:122px;height:35px;background:var(--blue);color:var(--white);font-family:"Open Sans",sans-serif;font-weight:700;font-size:15px;display:flex;align-items:center;justify-content:center;letter-spacing:.5px}
.footer-brand{position:absolute;left:895px;top:114px;font-family:"Open Sans",sans-serif;font-weight:400;font-size:56px;letter-spacing:2px;color:#8f8f8f;line-height:58px}
.footer-social{position:absolute;left:960px;top:202px;display:flex;gap:9px}
.footer-social span{width:25px;height:25px;border-radius:50%;background:var(--blue)}

.copyright{left:0;top:2236px;width:1200px;height:48px;background:var(--blue);color:var(--white);font-family:"Open Sans",sans-serif;font-size:14px;display:flex;align-items:center;justify-content:center}
</style>
</head>
<body>

<div class="abs topbar">
  <div class="contacts">
    <svg viewBox="0 0 24 24"><path d="M6.6 10.8a15 15 0 0 0 6.6 6.6l2.2-2.2a1 1 0 0 1 1-.25 11.4 11.4 0 0 0 3.6.6 1 1 0 0 1 1 1V20a1 1 0 0 1-1 1A17 17 0 0 1 3 4a1 1 0 0 1 1-1h3.5a1 1 0 0 1 1 1c0 1.25.2 2.45.6 3.6a1 1 0 0 1-.25 1z"/></svg>
    <span>(916) 555-0142 &nbsp;/&nbsp; (925) 555-0187</span>
    <span style="opacity:.6;margin-left:10px">|</span>
    <span class="mail"><svg viewBox="0 0 24 24"><path d="M2 5h20v14H2zM4 7v.5l8 5 8-5V7l-8 5z"/></svg>info@marwickostrand.com</span>
  </div>
  <div class="social"><span></span><span></span><span></span><span></span></div>
</div>

<header class="abs header">
  <div class="brand">MOLAW</div>
  <nav class="nav">
    <a class="active" style="left:676px">Home</a>
    <a style="left:762px">About Us<span class="caret">&#8964;</span></a>
    <a style="left:879px">Practice Areas<span class="caret">&#8964;</span></a>
    <a style="left:1031px">Contact Us</a>
  </nav>
</header>

<section class="abs hero" role="img" aria-label="Attorney standing with arms crossed in front of the California State Capitol dome framed by palm trees">
  <svg class="hero-arrow" style="left:34px" viewBox="0 0 20 30"><path d="M15 4 5 15l10 11"/></svg>
  <svg class="hero-arrow" style="left:1140px" viewBox="0 0 20 30"><path d="M5 4l10 11L5 26"/></svg>
  <div class="hero-text">MARWICK OSTRAND LAW<br>STRONG REPUTATIONS DON’T<br>GO UNNOTICED.</div>
  <div class="hero-cta">FREE CONSULTATION</div>
</section>

<section class="abs services">
  <h2 class="section-title" style="top:54px">OUR <em>SERVICES</em></h2>
  <div class="title-rule" style="top:107px"></div>
  <p class="lead" style="left:140px;width:920px;top:125px">Lorem Ipsum is simply dummy text of the printing and typesetting industry. Lorem Ipsum has been the industry’s standard dummy text ever since the 1500s, when an unknown printer took a galley of type and scrambled it to make a type specimen book.</p>

  <div class="service" style="left:70px">
    <svg viewBox="0 0 52 52"><circle cx="16" cy="7" r="5"/><path d="M10 14h12v18h-3v16h-6V32h-3z"/><rect x="24" y="16" width="22" height="2"/><rect x="34" y="16" width="2" height="26"/><path d="M27 19l-5 11h10zM43 19l-5 11h10z" opacity=".9"/><rect x="29" y="42" width="12" height="3"/></svg>
    <h3>BUSINESS LAW</h3>
    <p>Lorem Ipsum is simply dummy text of the prin and<br>typesetting &nbsp;text of industry orem</p>
  </div>
  <div class="service" style="left:437px">
    <svg viewBox="0 0 52 52"><path d="M26 3 2 25l3 3 3-2.8V49h36V25.2l3 2.8 3-3zM12 22 26 9l14 13v23H12z"/><path d="M19 28l6-6 4 4-6 6zM26 30l3-3 9 9-3 3zM17 40h14v3H17z"/></svg>
    <h3>REAL ESTATE LAW</h3>
    <p>Lorem Ipsum is simply dummy text of the prin and<br>typesetting &nbsp;text of industry orem</p>
  </div>
  <div class="service" style="left:802px">
    <svg viewBox="0 0 52 52"><path d="M16 18a12 12 0 1 0 0.01 0zm0 5a7 7 0 1 1-.01 0z"/><path d="M36 10a13 13 0 1 0 .01 0zm0 5a8 8 0 1 1-.01 0z"/><rect x="22" y="20" width="6" height="5"/></svg>
    <h3>CRIMINAL LAW</h3>
    <p>Lorem Ipsum is simply dummy text of the prin and<br>typesetting &nbsp;text of industry orem</p>
  </div>
</section>

<section class="abs welcome">
  <h2 class="section-title" style="top:53px">WELCOME TO <em>MOLAW</em></h2>
  <div class="title-rule" style="top:105px"></div>
  <p class="lead" style="left:100px;width:1000px;top:128px;font-size:14px;line-height:25.5px">After practicing in both the private and public sector for several years, Nadia Marwick and Arun Ostrand joined their legal expertise and formed Marwick Ostrand Law in 2015. &nbsp;With a combined 15 years of experience, Nadia and Arun specialize in Civil Litigation, Family Law, Immigration and Criminal Defense. Their goal is to provide their clients with the best possible outcome in each and every case.</p>
  <div class="btn-outline" style="left:524px;top:225px;width:151px;height:40px">READ MORE</div>
</section>

<section class="abs video">
  <h2 class="section-title" style="top:53px">WATCH <em>VIDEO</em></h2>
  <div class="title-rule" style="top:105px"></div>
  <p class="lead" style="left:200px;width:800px;top:128px">Lorem Ipsum is simply dummy text of the printing and typesetting industry. Lorem Ipsum has been the inext ever since the 1500s when an unknown printer took a galley of type and scrambled it to make a type en book.</p>
  <div class="video-media" role="img" aria-label="Hands holding a tablet playing a video of the two attorneys in an office with a brick wall"></div>
  <div class="play"><svg viewBox="0 0 14 18"><path d="M0 0l14 9-14 9z"/></svg></div>
</section>

<footer class="abs footer">
  <h4 style="left:88px">QUICK LINKS</h4>
  <ul class="quick-links">
    <li>- Home</li><li>- About Us</li><li>- Practice Areas</li><li>- Business Law</li><li>- Real Estate Law</li><li>- Criminal Law</li><li>- Contact Us</li>
  </ul>
  <div class="divider" style="left:271px"></div>

  <h4 style="left:318px">CONTACT INFO</h4>
  <div class="contact-list">
    <div class="contact-row" style="top:0"><svg viewBox="0 0 12 14"><path d="M6 0a5 5 0 0 0-5 5c0 4 5 9 5 9s5-5 5-9a5 5 0 0 0-5-5zm0 7a2 2 0 1 1 0-4 2 2 0 0 1 0 4z"/></svg><span>MOLAW<br>418 Capitol Row, Suite 200<br>Sacramento, CA 95814</span></div>
    <div class="contact-row" style="top:82px"><svg viewBox="0 0 24 24"><path d="M6.6 10.8a15 15 0 0 0 6.6 6.6l2.2-2.2a1 1 0 0 1 1-.25 11.4 11.4 0 0 0 3.6.6 1 1 0 0 1 1 1V20a1 1 0 0 1-1 1A17 17 0 0 1 3 4a1 1 0 0 1 1-1h3.5a1 1 0 0 1 1 1c0 1.25.2 2.45.6 3.6a1 1 0 0 1-.25 1z"/></svg><span>(916) 555-0142</span></div>
    <div class="contact-row" style="top:119px"><svg viewBox="0 0 12 14"><path d="M3 0h6v4H3zM0 5h12v7H0zM3 9h6v5H3z"/></svg><span>(916) 555-0143</span></div>
    <div class="contact-row" style="top:156px"><svg viewBox="0 0 24 24"><path d="M2 5h20v14H2zM4 7v.5l8 5 8-5V7l-8 5z"/></svg><span>info@marwickostrand.com</span></div>
  </div>
  <div class="divider" style="left:522px"></div>

  <h4 style="left:556px">QUICK INQUIRY</h4>
  <div class="field" style="top:97px;height:35px">Your Name</div>
  <div class="field" style="top:141px;height:35px">Email</div>
  <div class="field" style="top:187px;height:48px">Message</div>
  <div class="submit">SUBMIT</div>
  <div class="divider" style="left:860px"></div>

  <div class="footer-brand">MOLAW</div>
  <div class="footer-social"><span></span><span></span><span></span></div>
</footer>

<div class="abs copyright">Copyright © 2017 MOLAW. All Right Reserved</div>

</body>
</html>
```